Business Cards for Bramblewood Coatings Pty Ltd

Hi every one i need a design for my buisness cards. I Want my logo in it and the name of the company needs to stand out Bramblewood Coatings Pty Ltd. I want the background of the buisness cards black and i want the font to stand out in either a white or a silver stylish text. I want the design to be simple but original not to in your face if you know what i mean. I want on the back of the buisness cards to have the services that my buisness offers.
• Interior/Exterior
• Residential/Commercial
• Special effects/Texture Coatings
• Water Damage Repair
• Fully qualified
• Pensioner Discount
• 10 Year guarantee
• Fully Insured
• Obligation free quotes
full internal repaints include a proffesionla cleaning service
I want the services on the back to be layed out in an originall way not just dot points. If possible could my logo take up the whole back ground of the back but the text with the services be kind of like transparent so u cvan still see the logo i dont know if its possible it woiuld just look cool if possible. When i pick a design ill give my contact details to the designer to add to the design at the end. Any questions please just ask! Ill upload my logo.
Conatcs will include office phone: Mobile: E-mail - dean@bramblewoodcoatings.com.au, Ill also have a Postal address which is a PO Box and my website is www.bramblewoodcoatings.com.au

```html
<!DOCTYPE html>
<html lang="en">
<head>
<meta charset="utf-8">
<title>Bramblewood Coatings Pty Ltd – Business Cards</title>
<link rel="stylesheet" href="https://fonts.googleapis.com/css2?family=Open+Sans:wght@400;600;700&display=swap">
<style>
  :root {
    --page: #ffffff;
    --card-black: #000000;
    --card-white: #ffffff;
    --ink: #1a1a1a;
    --lime: #8dc63f;
    --leaf: #2e8b3c;
    --silver: #e8e8e8;
    --edge: #222222;
  }
  * { box-sizing: border-box; margin: 0; padding: 0; }
  html, body {
    width: 1200px; height: 900px; overflow: hidden;
    background: var(--page);
    font-family: "Open Sans", Arial, sans-serif;
  }
  .canvas { position: relative; width: 1200px; height: 900px; }

  .card {
    position: absolute; top: 74px;
    width: 424px; height: 763px;
    border: 1.5px solid var(--edge);
    overflow: hidden;
  }

  /* Front */
  .card--front { left: 169px; background: var(--card-black); }
  .brand-mark {
    position: absolute; left: 164px; top: 117px;
    width: 130px; height: 130px;
    background: var(--lime); border-radius: 8px;
  }
  .brand-name {
    position: absolute; left: 0; width: 424px; top: 270px;
    text-align: center; color: var(--silver);
    font-weight: 700; text-transform: uppercase;
    font-size: 25px; line-height: 32px; letter-spacing: 0.5px;
  }
  .contact-list { position: absolute; left: 0; top: 470px; list-style: none; width: 424px; }
  .contact-item {
    position: absolute; left: 0; height: 30px; width: 424px;
    display: flex; align-items: center;
    color: var(--lime); font-size: 16px;
  }
  .contact-icon { position: absolute; left: 62px; width: 24px; height: 22px; display: flex; align-items: center; justify-content: center; }
  .contact-icon svg { width: 22px; height: 20px; }
  .contact-icon--text { font-size: 15px; color: var(--lime); font-style: italic; }
  .contact-text { position: absolute; left: 118px; white-space: nowrap; }
  .contact-item--phone  { top: 0; }
  .contact-item--mobile { top: 44px; }
  .contact-item--web    { top: 90px; }
  .contact-item--email  { top: 137px; }
  .contact-item--post   { top: 176px; }

  /* Back */
  .card--back { left: 625px; background: var(--card-white); }
  .back-corner { position: absolute; left: 0; top: 0; width: 424px; height: 763px; }
  .service-list {
    position: absolute; top: 40px; left: 0; width: 424px;
    font-size: 19.5px; color: var(--ink);
  }
  .service-line { display: block; text-align: right; line-height: 39.5px; white-space: nowrap; padding-right: 17px; }
  .service-line--l8  { padding-right: 26px; }
  .service-line--l9  { padding-right: 26px; }
  .service-line--l10 { padding-right: 47px; }
  .service-line--l11 { padding-right: 126px; }
  .service-line--l12 { padding-right: 165px; }
  .service-line--l13 { padding-right: 205px; }
  .service-line--l14 { padding-right: 244px; }
  .accent-lime { color: var(--lime); }
  .accent-leaf { color: var(--leaf); }

  .back-mark {
    position: absolute; left: 284px; top: 615px;
    width: 61px; height: 61px; background: var(--lime); border-radius: 5px;
  }
  .back-name {
    position: absolute; left: 200px; width: 224px; top: 686px;
    text-align: center; color: var(--silver);
    font-weight: 700; font-size: 12px; line-height: 17px; text-transform: uppercase;
  }
</style>
</head>
<body>
<main class="canvas">

  <section class="card card--front" aria-label="Business card front">
    <div class="brand-mark" aria-hidden="true"></div>
    <h1 class="brand-name">Bramblewood Coatings<br>Pty Ltd</h1>

    <ul class="contact-list">
      <li class="contact-item contact-item--phone">
        <span class="contact-icon" aria-label="Office phone">
          <svg viewBox="0 0 22 20"><path d="M2 7 Q11 1 20 7 L18 10 L15 8 L15 6 Q11 4.5 7 6 L7 8 L4 10 Z" fill="none" stroke="#8dc63f" stroke-width="1.3"/><rect x="5" y="11" width="12" height="7" rx="1" fill="none" stroke="#8dc63f" stroke-width="1.3"/></svg>
        </span>
        <span class="contact-text"></span>
      </li>
      <li class="contact-item contact-item--mobile">
        <span class="contact-icon" aria-label="Mobile">
          <svg viewBox="0 0 22 20"><rect x="5" y="1" width="12" height="18" rx="1.5" fill="none" stroke="#8dc63f" stroke-width="1.4"/><rect x="7.5" y="4" width="7" height="7" fill="#8dc63f"/></svg>
        </span>
        <span class="contact-text"></span>
      </li>
      <li class="contact-item contact-item--web">
        <span class="contact-icon contact-icon--text" aria-label="Website">www</span>
        <span class="contact-text">www.bramblewoodcoatings.com.au</span>
      </li>
      <li class="contact-item contact-item--email">
        <span class="contact-icon contact-icon--text" aria-label="Email">@</span>
        <span class="contact-text">dean@bramblewoodcoatings.com.au</span>
      </li>
      <li class="contact-item contact-item--post">
        <span class="contact-icon" aria-label="Postal address">
          <svg viewBox="0 0 22 20"><rect x="2" y="4" width="18" height="12" fill="none" stroke="#8dc63f" stroke-width="1.4"/><path d="M2 4 L11 11 L20 4" fill="none" stroke="#8dc63f" stroke-width="1.4"/></svg>
        </span>
        <span class="contact-text"></span>
      </li>
    </ul>
  </section>

  <section class="card card--back" aria-label="Business card back">
    <svg class="back-corner" viewBox="0 0 424 763" aria-hidden="true">
      <polygon points="424,422 424,763 102,763" fill="#000000"/>
    </svg>

    <p class="service-list">
      <span class="service-line">Interior/Exterior •</span>
      <span class="service-line">Residential /Commercial•</span>
      <span class="service-line"><span class="accent-lime">Water damage repairs</span> •</span>
      <span class="service-line">Plaster repairs • Wall paper</span>
      <span class="service-line">removal • Special effect</span>
      <span class="service-line">feature walls • Exterior texture</span>
      <span class="service-line">coatings &nbsp;• <span class="accent-leaf">Colour consultations</span></span>
      <span class="service-line service-line--l8">• Full internal repaints include</span>
      <span class="service-line service-line--l8">a free professional cleaning</span>
      <span class="service-line service-line--l9">service • Fully qualified •</span>
      <span class="service-line service-line--l10">Fully Insured •</span>
      <span class="service-line service-line--l11 accent-lime">10 year guarantee •</span>
      <span class="service-line service-line--l12">Pensioner <span class="accent-lime">discounts</span> •</span>
      <span class="service-line service-line--l13">Obligation free</span>
      <span class="service-line service-line--l14">quotes</span>
    </p>

    <div class="back-mark" aria-hidden="true"></div>
    <p class="back-name">Bramblewood Coatings<br>Pty Ltd</p>
  </section>

</main>
</body>
</html>
```